Media company needs a dales aid for customers and suppliers

We need a brochure design for a new media company called Talcomb Media. We provide retailers with a retail solutions supplying DVDs, CDs and games on a promotional or a category managed service. We refurbish and recycle used media product to a like new standard.

We also buy overstocks from all the major film studios and music labels

We have just had a design agreed for the logo (through KP).

We need this as a 'show and tell' piece to visit retailers so they understand the concept and choose the display options (cardboard FSDU- games/dvd/CD.

It is almost a menu - capability then options.
Updates

Updated content for inclusion

Target Market(s)

Retailers, and potential suppliers. We are into DVD/CD and Games- the design must not be too music orientated

Industry/Entity Type

Graphic Design

Font styles to use
Serif

Requirements
Must have
• Different, not a A4 piece
• Would like the size to fit in a DVD case. Would also need a introductory sleeve that can go in the front of the DVD box. Then we can use in the DVD box or just on its own.
• We have a few 'tag lines'
• Revive the entertainment category
• Recycle the product and re-engage the consumer
• Reinvesting in retail

```html
<!DOCTYPE html>
<html lang="en">
<head>
<meta charset="utf-8">
<title>Talcomb Media – Brochure Cards</title>
<link href="https://fonts.googleapis.com/css2?family=Questrial&display=swap" rel="stylesheet">
<style>
  :root {
    --backdrop: #ececec;
    --card: #f7f7f8;
    --navy: #1f3573;
    --disc-light: #e6ecf7;
    --disc-mid: #9db3dc;
    --disc-deep: #5a78b8;
    --dot-tint: #cfdcf0;
    --leaf: #4fae3a;
  }
  * { box-sizing: border-box; margin: 0; padding: 0; }
  html, body {
    width: 1200px; height: 954px; overflow: hidden;
    background: var(--backdrop);
    font-family: "Questrial", "Century Gothic", sans-serif;
    color: var(--navy);
  }
  .spread {
    position: relative; width: 1200px; height: 954px;
    display: flex; justify-content: center; align-items: center; gap: 90px;
  }
  .card {
    position: relative; width: 460px; height: 640px;
    background: var(--card);
    overflow: hidden;
  }
  /* Front cover */
  .front .halftone {
    position: absolute; left: 0; top: 0; width: 100%; height: 100%;
    background: linear-gradient(160deg, var(--card) 0%, var(--card) 20%, var(--dot-tint) 55%, var(--card) 85%);
    opacity: .6;
  }
  .brand {
    position: absolute; display: flex; align-items: center; gap: 10px;
  }
  .front .brand { left: 42px; top: 150px; }
  .brand-dot {
    width: 34px; height: 34px; border-radius: 50%; background: var(--navy);
  }
  .brand-name { font-size: 34px; line-height: 1; letter-spacing: .5px; }
  .brand-sub { display: block; font-size: 9px; letter-spacing: 7px; margin-top: 3px; }
  .range {
    position: absolute; left: 42px; top: 218px;
    display: flex; gap: 46px; font-size: 17px; letter-spacing: 1px;
  }
  .front .disc-art {
    position: absolute; right: 0; bottom: 0; width: 340px; height: 400px;
    background: radial-gradient(circle at 60% 55%, var(--disc-light) 0%, var(--disc-mid) 55%, var(--disc-deep) 100%);
    border-top-left-radius: 220px 200px;
  }
  /* Back cover */
  .back .disc-art {
    position: absolute; left: 0; top: 0; width: 300px; height: 260px;
    background: linear-gradient(135deg, var(--disc-mid) 0%, var(--disc-light) 55%, var(--leaf) 100%);
    border-bottom-right-radius: 150px 130px;
  }
  .back .edge-arc { position: absolute; right: 0; top: 300px; }
  .back .brand { left: 42px; top: 470px; }
  .address {
    position: absolute; left: 42px; top: 540px;
    font-size: 12px; letter-spacing: 1px; line-height: 1.9; text-transform: uppercase;
  }
</style>
</head>
<body>
<main class="spread">
  <section class="card front">
    <div class="halftone" role="img" aria-label="Soft blue halftone dot pattern"></div>
    <div class="brand">
      <span class="brand-dot"></span>
      <span class="brand-name">Talcomb<span class="brand-sub">MEDIA LTD</span></span>
    </div>
    <ul class="range" style="list-style:none">
      <li>DVD'S</li><li>CD'S</li><li>GAMES</li>
    </ul>
    <div class="disc-art" role="img" aria-label="Cluster of overlapping blue and silver discs"></div>
  </section>

  <section class="card back">
    <div class="disc-art" role="img" aria-label="Large silver disc with green recycling arrows"></div>
    <svg class="edge-arc" width="60" height="160" viewBox="0 0 60 160" aria-hidden="true">
      <path d="M60 0 A80 80 0 0 0 60 160" fill="none" stroke="var(--navy)" stroke-width="12"/>
    </svg>
    <div class="brand">
      <span class="brand-dot"></span>
      <span class="brand-name">Talcomb<span class="brand-sub">MEDIA LTD</span></span>
    </div>
    <address class="address" style="font-style:normal">
      110B, Lorem Ipsum, Lorem Lorem Ipsum<br>
      Ipsum - 110011
    </address>
  </section>
</main>
</body>
</html>
```